Vehcile and Personal GPS Tracking Service Needs Brochure

We need a brochure design for our serviced called Harbor Beacon Locate (HBL) www.harborbeaconlocate.com (info site) & www.harborbeaconlocate.net (our actually gps tracking site).

HBL provides a Live GPS Tracking service for vehicles and personal trackers (key tag size).

We need a brochure that will describe our products and its benefits.

The use of our product allows corporate companies to track their vehcile fleets and security their goods and vehciles.

Security is a big issues in our country. Car theif is common. Also, kidnapping of CEOs is a concern.

Our target audience are corporate companys, who are interested in managing their vehcile fleets and ensuring the security of their vehicles and staff memebers.

We would like to continue using the corporate colours of yellow and grey.

The design should communicate reliablity and safety.

Target Market(s)

Medium to large companies (10 or more vehciles). CEOs.

Industry/Entity Type

Security

Requirements
Must have
• Plese see the attached word document that we are providing customers.
Nice to have
• It would be good to have a picture of a vehcile being tracking on a map, so people have a visual of how it works.
Should not have
• The brouchure should not include pricing, as this may change. However, we would like to show that we hae to different rates for self montioring and security monitoring.

```html
<!DOCTYPE html>
<html lang="en">
<head>
<meta charset="utf-8">
<title>Harbor Beacon Locate – Live GPS Tracking Brochure</title>
<link rel="stylesheet" href="https://fonts.googleapis.com/css2?family=Didact+Gothic&family=Questrial&family=Pinyon+Script&display=swap">
<style>
  :root {
    --brand-grey: #8b8b8d;
    --brand-yellow: #f6d10c;
    --brand-orange: #f39a1e;
    --text-light: #ffffff;
    --photo-sky: #9aa9b4;
    --photo-street: #7f8780;
    --photo-warm: #a08f7c;
    --badge-gold: #c9a24a;
    --badge-gold-light: #ecd493;
    --device-silver: #c7c9cc;
    --device-screen: #e9e4d6;
    --line: 17.2px;
  }
  * { margin: 0; padding: 0; box-sizing: border-box; }
  html, body { width: 1200px; height: 848px; overflow: hidden; background: var(--brand-grey); }
  .brochure {
    position: relative;
    width: 1200px;
    height: 848px;
    overflow: hidden;
    font-family: "Didact Gothic", "Questrial", sans-serif;
    color: var(--text-light);
    font-size: 11.2px;
    line-height: var(--line);
  }
  .street-photo {
    position: absolute; left: 0; top: 0; width: 1200px; height: 340px;
    background: linear-gradient(180deg, var(--photo-sky) 0%, var(--photo-warm) 35%, var(--photo-street) 70%, #6d726c 100%);
  }
  .backdrop { position: absolute; left: 0; top: 0; }
  .laptop-map {
    position: absolute; left: 482px; top: 24px; width: 256px; height: 200px;
    background: linear-gradient(160deg, var(--device-screen) 0%, var(--device-screen) 58%, var(--device-silver) 60%, #9ea1a5 100%);
    border-radius: 6px;
  }
  .warranty-badge {
    position: absolute; left: 742px; top: 120px; width: 112px; height: 106px;
    border-radius: 50%;
    background: radial-gradient(circle at 40% 35%, var(--badge-gold-light), var(--badge-gold) 70%);
  }
  .column { position: absolute; white-space: nowrap; }
  .ln { display: block; height: var(--line); }
  .ln.hang { padding-left: 14px; }
  .ln.lead { padding-left: 37px; }
  .ln.nudge { padding-left: 14px; }
  .col-intro { left: 38px; top: 326px; }
  .col-features { left: 303px; top: 244px; }
  .col-security { left: 619px; top: 234px; }
  .col-personal { left: 909px; top: 303px; }
  .drop-cap {
    position: absolute; left: 20px; top: 290px;
    font-family: "Pinyon Script", cursive;
    font-size: 66px;
    line-height: 70px;
    color: var(--text-light);
  }
  .section-title {
    font-family: "Questrial", sans-serif;
    font-weight: 700;
    color: var(--brand-orange);
    font-size: 14.5px;
  }
  .term { font-weight: 700; }
  .bottom-stripe-light { position: absolute; left: 0; top: 823px; width: 1200px; height: 4px; background: #d9d9d9; }
  .bottom-stripe { position: absolute; left: 0; top: 827px; width: 1200px; height: 7px; background: linear-gradient(90deg, var(--brand-orange), var(--brand-yellow) 50%, var(--brand-orange)); }
</style>
</head>
<body>
<main class="brochure">
  <div class="street-photo" role="img" aria-label="Photograph of a busy town street with parked cars, trucks and pedestrians"></div>

  <svg class="backdrop" width="1200" height="848" viewBox="0 0 1200 848" aria-hidden="true">
    <path d="M0,305 Q600,60 1200,182 L1200,848 L0,848 Z" fill="var(--brand-yellow)"/>
    <path d="M0,322 Q600,120 1200,248 L1200,848 L0,848 Z" fill="var(--brand-grey)"/>
  </svg>

  <div class="laptop-map" role="img" aria-label="Laptop showing a street map with a vehicle location marker, beside a computer mouse"></div>
  <div class="warranty-badge" role="img" aria-label="One year warranty seal"></div>

  <span class="drop-cap" aria-hidden="true">W</span>

  <section class="column col-intro">
    <span class="ln lead">elcome to Harbor Beacon Locate</span>
    <span class="ln">services. Our website offers real time, live GPS</span>
    <span class="ln">tracking services.</span>
    <span class="ln"></span>
    <span class="ln">Using GPS satellite technology, Harbor Beacon</span>
    <span class="ln">Locate's service enables you to see a vehicle or</span>
    <span class="ln">person move on a computer screen in real time.</span>
    <span class="ln">This enables you to know precisely where the car</span>
    <span class="ln">or person is. Our car tracking service can be used</span>
    <span class="ln">to track at any type of a vehicle or a fleet of</span>
    <span class="ln">vehicles. Our hand held personal trackers can be</span>
    <span class="ln">carried by anyone.</span>
    <span class="ln"></span>
    <span class="ln">The tracking system can be accessed at any time</span>
    <span class="ln">from a computer in the privacy of your own office</span>
    <span class="ln">or home or on an internet mobile device (tablet or</span>
    <span class="ln">smart phone), enabling you to see a car's or</span>
    <span class="ln">person's path in real time. You do not need to</span>
    <span class="ln">purchase or install any special software on your</span>
    <span class="ln">computer – our service enables you to track a</span>
    <span class="ln">vehicle or person live from anywhere you have</span>
    <span class="ln">internet connection.</span>
    <span class="ln"></span>
    <h2 class="ln section-title">Vehicle Live Tracking</h2>
    <span class="ln">Our Vehicle Live Tracking offers the following</span>
    <span class="ln">features:</span>
    <span class="ln"></span>
    <span class="ln">• &nbsp;<span class="term">Live Tracking:</span> Works from GPS location and</span>
  </section>

  <section class="column col-features">
    <span class="ln hang">communicating by GPRS network, you can</span>
    <span class="ln hang">log onto our website to view the exact</span>
    <span class="ln hang">location of your vehicle on StreetGrid maps and</span>
    <span class="ln hang">the direction of the traveling vehicle.</span>
    <span class="ln">• &nbsp;<span class="term">History</span>: Our web site stores history of the</span>
    <span class="ln hang">vehicle, enabling you to view the actual</span>
    <span class="ln hang">route of the vehicle has taken in the past,</span>
    <span class="ln hang">displayed on maps.</span>
    <span class="ln">• &nbsp;<span class="term">Report:</span> Our website provides you with useful</span>
    <span class="ln hang">information on our vehicle:</span>
    <span class="ln"></span>
    <span class="ln"><span class="term">Stop Report</span>: The location your vehicle is stopping and</span>
    <span class="ln">for how long</span>
    <span class="ln"><span class="term">Distance Report</span>: The distance your vehicle travels</span>
    <span class="ln">within a certain period</span>
    <span class="ln"><span class="term">Speed Report</span>: The speed your vehicle is travelling</span>
    <span class="ln"><span class="term">SOS Alarm:</span> The time and location of SOS Alarm</span>
    <span class="ln">activation</span>
    <span class="ln">Report format – All reports can be exported to PDF or</span>
    <span class="ln">GridSheet format</span>
    <span class="ln"></span>
    <span class="ln">• &nbsp;<span class="term">Alarms:</span> All our units have to ability to set the</span>
    <span class="ln hang">following alarms:</span>
    <span class="ln"><span class="term">Geo-fence:</span> A geo-fence (parameter) can be set for</span>
    <span class="ln">your vehicle. An alarm will be activated when the</span>
    <span class="ln">vehicle travels outside of the geo-fence.</span>
    <span class="ln"><span class="term">SOS Alarm:</span> Each vehicle is fitted with a push button</span>
    <span class="ln">SOS Alarm located under the steering column or near</span>
    <span class="ln">the ignition key.</span>
    <span class="ln"><span class="term">Low Power Alarm:</span> This alarm will indicated low power</span>
    <span class="ln">to the tracking unit.</span>
    <span class="ln">All alarms can be handled can be view on one page.</span>
  </section>

  <section class="column col-security">
    <span class="ln">Our Vehicle Live Tracking Service offers the following</span>
    <span class="ln">security features:</span>
    <span class="ln"></span>
    <span class="ln">• &nbsp;<span class="term">SOS Button:</span> It has three programmable call</span>
    <span class="ln">buttons. SOS, call 1 and call 2 which can be</span>
    <span class="ln">programmed to a security officer or family /</span>
    <span class="ln">friends. When the SOS button is pressed, the</span>
    <span class="ln">personal tracker will send a SMS to the</span>
    <span class="ln">pre-programmed number on the SOS button</span>
    <span class="ln">with a distress call. It will also give the Latitude</span>
    <span class="ln">&amp; Longitude of your location.&nbsp; An SOS Alarm</span>
    <span class="ln">will also be activated on our website.&nbsp; The</span>
    <span class="ln nudge">SOS Report will provide your exactly locations</span>
    <span class="ln">on StreetGrid Maps.</span>
    <span class="ln">• &nbsp;<span class="term">Disable Engine:</span>&nbsp; Vehicle fitted with our GPS</span>
    <span class="ln">tracking units can disable the engine via SMS.</span>
    <span class="ln">• &nbsp;Live tracking of vehicle: You vehicle can be</span>
    <span class="ln">tracked lived by yourself and/or your Security</span>
    <span class="ln">Service.</span>
    <span class="ln"></span>
    <h2 class="ln section-title">Benefits of Vehicle Live Tracking</h2>
    <span class="ln">If you are a business owner, you can have more</span>
    <span class="ln">control on your employees and inventory time through</span>
    <span class="ln">our live tracking services. If you are a goods</span>
    <span class="ln">dispatcher, our service offers you an effective and</span>
    <span class="ln">simple solution to help you make your deliveries on</span>
    <span class="ln">time. No matter what industry you serve, tracking your</span>
    <span class="ln">vehicles can help you.</span>
    <span class="ln">Benefits of our Vehicle Live Tracking:</span>
    <span class="ln"></span>
    <span class="ln"></span>
    <span class="ln">• &nbsp;Boost the security of your vehicles and</span>
    <span class="ln hang">staff members</span>
    <span class="ln">• &nbsp;Increase the likelihood of vehicle theft recovery</span>
  </section>

  <section class="column col-personal">
    <span class="ln">• &nbsp;Track your vehicles, inventory and</span>
    <span class="ln hang">employees</span>
    <span class="ln">• &nbsp;Boost your business' efficiency and</span>
    <span class="ln hang">profitability by using our tracking services</span>
    <span class="ln">• &nbsp;Serve your customers better by making</span>
    <span class="ln hang">fast deliveries</span>
    <span class="ln">• &nbsp;Manage your business' assets and</span>
    <span class="ln hang">resources in a more effective manner</span>
    <span class="ln"></span>
    <span class="ln">Please visit our information website for &nbsp;&nbsp;&nbsp;&nbsp; further</span>
    <span class="ln">information: www.harborbeaconlocate.com</span>
    <span class="ln"></span>
    <h2 class="ln section-title">Personal Trackers</h2>
    <span class="ln">Harbor Beacon Locate offers Personal Trackers.</span>
    <span class="ln">Harbor Beacon Locate's Personal Tracker is a small</span>
    <span class="ln">device that enables you to remotely track, in real</span>
    <span class="ln">time, the position of a loved one or an important</span>
    <span class="ln">asset. Through our website, you can immediately</span>
    <span class="ln">know the position of your beloved one or asset</span>
    <span class="ln">through this devise. The tracker uses GPS</span>
    <span class="ln">technology, cellular phone communication and</span>
    <span class="ln">the Internet to provide you with its precise</span>
    <span class="ln">location in seconds.</span>
    <span class="ln">The tracker can be used for many purposes –</span>
    <span class="ln">your high value assets such as your boat or car,</span>
    <span class="ln">your children or elderly parents – enabling you to</span>
    <span class="ln">locate them quickly in the event there is cause</span>
    <span class="ln">for concern.</span>
  </section>

  <div class="bottom-stripe-light"></div>
  <div class="bottom-stripe"></div>
</main>
</body>
</html>
```